依頼詳細
落ち着いたBARのフライヤーの裏面を作成してください。
表面はロゴだけ印刷します(ロゴは添付ファイル参照ください)
ロゴの世界観を壊さないよう願います。
住所から地図を作成してください。
記載項目
1時間3,000円(税別)
延長 2,500円(税別)
スタッフドリンク 500円~
フード各種 500円~

営業時間 20時~LAST
休日 日曜日・祝日(祝日の前日が日曜日の場合、営業します)
尼崎市柳瀬町4-7-15 ルミエビル2F
電話番号(未定)
サイズ
14.8×10(横書)
ページ数
片面
希望イメージ
シンプル 複雑
単色 カラフル
暗い 明るい
日常 高級
遊び心 厳粛
未来的 伝統的
女性的 男性的
希望する色
グレー系
納品ファイル
• 高解像度JPG (.jpg)
• イラストレーター形式 (.ai)
• フォトショップ形式 (.psd)
• PNG形式 (.png)
補足説明

```html
<!DOCTYPE html>
<html lang="ja">
<head>
<meta charset="utf-8">
<title>BAR ASHWOOD フライヤー</title>
<link href="https://fonts.googleapis.com/css2?family=Noto+Serif+JP:wght@400;600&display=swap" rel="stylesheet">
<style>
:root{
  --page:#ffffff;
  --leather-dark:#0e0e0e;
  --leather-mid:#2a2a2a;
  --silver:#e4e2dc;
  --text:#d8d6d0;
  --muted:#a9a7a2;
  --label-bg:#e9e7e2;
  --label-text:#1a1a1a;
  --line:#8d8b86;
}
*{margin:0;padding:0;box-sizing:border-box}
html,body{width:867px;height:1200px;overflow:hidden;background:var(--page)}
body{position:relative;font-family:"Noto Serif JP",serif;color:var(--text)}
.card{
  position:absolute;left:29px;width:809px;height:547px;overflow:hidden;
  background:radial-gradient(ellipse at 45% 35%,var(--leather-mid) 0%,#1a1a1a 55%,var(--leather-dark) 100%);
  box-shadow:0 2px 6px rgba(0,0,0,.25);
}
.card--front{top:35px}
.card--back{top:618px}
.wordmark{position:absolute;left:0;right:0;display:flex;align-items:center;justify-content:center;gap:16px;
  font-family:"Noto Serif JP",serif;font-weight:400;color:var(--silver);white-space:nowrap}
.wordmark-dot{background:var(--silver);flex:none}
.card--front .wordmark{top:210px;font-size:54px;letter-spacing:8px}
.card--front .wordmark-dot{width:10px;height:10px}
.card--back .wordmark{top:70px;font-size:32px;letter-spacing:5px;gap:12px}
.card--back .wordmark-dot{width:7px;height:7px}
.photo{position:absolute}
.photo--glass-top{right:0;top:0;width:170px;height:170px;
  background:radial-gradient(circle at 55% 50%,#5a5a5a 0%,#303030 45%,rgba(30,30,30,0) 75%)}
.photo--glass-left{left:0;top:245px;width:200px;height:302px;
  background:radial-gradient(ellipse at 45% 55%,#6b6b6b 0%,#2f2f2f 50%,#121212 90%)}
.info{position:absolute;left:170px;right:170px;top:160px;text-align:center}
.phone{font-size:28px;letter-spacing:3px;color:var(--silver);display:flex;align-items:center;justify-content:center;gap:12px}
.phone svg{width:22px;height:22px}
.hours,.holiday{font-size:13px;color:var(--muted);margin-top:8px;letter-spacing:1px}
.holiday{margin-top:4px;letter-spacing:0}
.price{position:absolute;left:222px;top:318px;width:182px}
.price-title{font-size:13px;letter-spacing:3px;color:var(--silver);margin-bottom:14px;text-align:center}
.price-title::before{content:"";display:inline-block;width:6px;height:6px;background:var(--silver);transform:rotate(45deg);margin-right:8px;vertical-align:2px}
.price-row{display:flex;align-items:center;justify-content:space-between;margin-bottom:13px;font-size:12px}
.price-label{background:var(--label-bg);color:var(--label-text);padding:2px 6px;font-size:10px;min-width:62px;text-align:center}
.price-value{color:var(--text);letter-spacing:.5px}
.map{position:absolute;left:428px;top:318px;width:250px;height:165px;
  background:linear-gradient(160deg,#3a3a3a,#242424);border:1px solid var(--line)}
.address{position:absolute;right:90px;top:508px;font-size:12px;color:var(--muted);letter-spacing:1px}
</style>
</head>
<body>
<section class="card card--front" aria-label="表面">
  <div class="wordmark"><span class="wordmark-dot"></span><span>BAR ASHWOOD</span></div>
</section>

<section class="card card--back" aria-label="裏面">
  <div class="photo photo--glass-top" role="img" aria-label="氷の入ったグラスの写真"></div>
  <div class="photo photo--glass-left" role="img" aria-label="カウンターに置かれたグラスの写真"></div>

  <div class="wordmark"><span class="wordmark-dot"></span><span>BAR ASHWOOD</span></div>

  <div class="info">
    <div class="phone">
      <svg viewBox="0 0 24 24" aria-hidden="true"><path fill="#e4e2dc" d="M6.6 10.8a15.1 15.1 0 0 0 6.6 6.6l2.2-2.2a1 1 0 0 1 1-.25 11.4 11.4 0 0 0 3.6.57 1 1 0 0 1 1 1V20a1 1 0 0 1-1 1A17 17 0 0 1 3 4a1 1 0 0 1 1-1h3.5a1 1 0 0 1 1 1c0 1.25.2 2.45.57 3.6a1 1 0 0 1-.25 1z"/></svg>
      <span>00-0000-0000</span>
    </div>
    <p class="hours">営業時間 20時～LAST</p>
    <p class="holiday">休日 日曜日・祝日(祝日の前日が日曜日の場合、営業します)</p>
  </div>

  <div class="price">
    <div class="price-title">PRICE</div>
    <div class="price-row"><span class="price-label">1時間</span><span class="price-value">3,000円(税別)</span></div>
    <div class="price-row"><span class="price-label">延長</span><span class="price-value">2,500円(税別)</span></div>
    <div class="price-row"><span class="price-label">スタッフドリンク</span><span class="price-value">500円～</span></div>
    <div class="price-row"><span class="price-label">フード各種</span><span class="price-value">500円～</span></div>
  </div>

  <div class="map" role="img" aria-label="駅から店舗までの周辺地図"></div>

  <p class="address">尼崎市柳瀬町4-7-15 ルミエビル2F</p>
</section>
</body>
</html>
```